TerraVolt Biogas - converting waste into cash infographic

TerraVolt Biogas is an innovative energy from waste program that converts organic waste collected from tourist resorts and dairy farms in Jamaica into biogas for electricity generation. Participating resorts and farms receive a cash reward dependent on the quality and quantity of waste provided.

We need a creative infographic that communicates the process of converting waste into cash (see attached Waste to Cash sketch) using our branding, color scheme, and fonts (attached).

The infographic will be incorporated into our marketing materials, such as our website which is currently under construction, http://bentomire8841.sitebuild.example/terravolt2#!home/mainPage

Similar infographics can be found at http://pelmagrid.example/ and in the attached Pelmagrid teaser (page 2).

Finished product/file should be presented in jpeg, ai, and eps format.

Target Market(s)

hotel management, farmers, international development/sustainability professionals

Industry/Entity Type

Marketing

Requirements
Must have
• Use of TerraVolt Biogas' font and color scheme (attached).

```html
<!DOCTYPE html>
<html lang="en">
<head>
<meta charset="utf-8">
<title>TerraVolt Biogas – Waste to Cash</title>
<link rel="stylesheet" href="https://fonts.googleapis.com/css2?family=Nunito:wght@700;800&display=swap">
<style>
  :root {
    --sky: #29a8e0;
    --ocean: #0a6fb3;
    --ink: #1b7cc0;
    --paper: #ffffff;
  }
  html, body {
    margin: 0;
    padding: 0;
    width: 1200px;
    height: 695px;
    overflow: hidden;
    background: var(--paper);
  }
  .infographic {
    display: block;
    width: 1200px;
    height: 695px;
    font-family: "Nunito", "Arial Rounded MT Bold", sans-serif;
  }
  .source-art { fill: var(--sky); }
  .source-label {
    fill: var(--paper);
    font-weight: 800;
    font-size: 21px;
    text-anchor: middle;
  }
  .source-label--caps { font-size: 22px; letter-spacing: 0.5px; }
  .flow-arrow {
    stroke: var(--ink);
    stroke-width: 3;
    fill: none;
    marker-end: url(#arrowhead);
  }
  .output-ring { fill: var(--sky); }
  .output-core { fill: var(--ocean); stroke: var(--paper); stroke-width: 3; }
  .output-label {
    fill: var(--paper);
    font-weight: 800;
    font-size: 21px;
    text-anchor: middle;
  }
  .digestor-ring { fill: var(--sky); }
  .digestor-core { fill: var(--ocean); stroke: var(--paper); stroke-width: 3; }
  .digestor-label {
    fill: var(--paper);
    font-weight: 800;
    font-size: 52px;
    text-anchor: middle;
  }
</style>
</head>
<body>
<svg class="infographic" viewBox="0 0 1200 695" xmlns="http://www.w3.org/2000/svg">
  <defs>
    <marker id="arrowhead" viewBox="0 0 10 10" refX="8" refY="5" markerWidth="5" markerHeight="5" orient="auto">
      <path d="M0,0 L10,5 L0,10 z" fill="#1b7cc0"/>
    </marker>
  </defs>

  <!-- Inputs -->
  <g class="source source--hotels">
    <rect class="source-art" x="138" y="98" width="195" height="143" rx="4"
          role="img" aria-label="Hotel building illustration"/>
    <text class="source-label source-label--caps" x="235" y="160">HOTELS</text>
    <text class="source-label" x="235" y="186">food</text>
    <text class="source-label" x="235" y="212">waste</text>
  </g>

  <g class="source source--cow">
    <rect class="source-art" x="34" y="471" width="192" height="113" rx="14"
          role="img" aria-label="Cow illustration"/>
    <text class="source-label" x="104" y="502">cow</text>
    <text class="source-label" x="104" y="526">manure</text>
  </g>

  <g class="source source--pig">
    <rect class="source-art" x="179" y="524" width="179" height="98" rx="22"
          role="img" aria-label="Pig illustration"/>
    <text class="source-label" x="243" y="552">pig</text>
    <text class="source-label" x="243" y="576">manure</text>
  </g>

  <!-- Flow arrows -->
  <line class="flow-arrow" x1="245" y1="254" x2="301" y2="311"/>
  <line class="flow-arrow" x1="264" y1="499" x2="311" y2="433"/>
  <line class="flow-arrow" x1="593" y1="320" x2="650" y2="254"/>
  <line class="flow-arrow" x1="593" y1="430" x2="650" y2="499"/>
  <line class="flow-arrow" x1="627" y1="377" x2="739" y2="377"/>
  <line class="flow-arrow" x1="914" y1="377" x2="1017" y2="377"/>

  <!-- Digestor -->
  <g class="digestor">
    <ellipse class="digestor-ring" cx="456" cy="373" rx="156" ry="71"/>
    <ellipse class="digestor-core" cx="456" cy="373" rx="146" ry="61"/>
    <text class="digestor-label" x="456" y="390">digestor</text>
  </g>

  <!-- Outputs -->
  <g class="output output--biogas">
    <circle class="output-ring" cx="688" cy="183" r="62"/>
    <circle class="output-core" cx="688" cy="183" r="54"/>
    <text class="output-label" x="688" y="190">biogas</text>
  </g>

  <g class="output output--electricity">
    <circle class="output-ring" cx="820" cy="373" r="62"/>
    <circle class="output-core" cx="820" cy="373" r="54"/>
    <text class="output-label" x="820" y="368">clean</text>
    <text class="output-label" x="820" y="392">electricity</text>
  </g>

  <g class="output output--fertilizer">
    <circle class="output-ring" cx="688" cy="565" r="62"/>
    <circle class="output-core" cx="688" cy="565" r="54"/>
    <text class="output-label" x="688" y="572">fertilizer</text>
  </g>

  <g class="output output--cash">
    <circle class="output-ring" cx="1102" cy="373" r="62"/>
    <circle class="output-core" cx="1102" cy="373" r="54"/>
    <text class="output-label" x="1102" y="368">cash</text>
    <text class="output-label" x="1102" y="392">rewards</text>
  </g>
</svg>
</body>
</html>
```